依頼詳細
【依頼概要】
●依頼:
除菌スプレー(ソフィネット)のパッケージデザインを依頼します。

●ラインナップ:
ラインナップは2つで、大ボトル(500ml)と小ボトル(50ml)がございますが、
両方とも同様のパッケージにしたいと考えております。
※添付ファイル:大、小ボトル

●デザイン内に入れる文言:
商品名である「ソフィネット」(カタカナ、英字のどちらか。もしくは両方)

●ターゲット層:
「主婦層」、「小さなお子様がいらっしゃる家庭」

●今回のボトルリニューアルで訴求したいポイント
・愛着を持てる(動物や、ゆるキャラ的なかわいさ)
(ペンギンや白熊のデザインをイメージしておりますが、その他も幅広く募集します)
※添付ファイル:デザインラフ案
・ちょっとした遊び心がある
・子供にも好かれるかわいらしさ
・トイレやリビングなど、身近に置いておきたいと思える。
・(小型ボトルを)バッグに入れておきたいと思える。
・インパクトがあり、手に取りたくなる

●カラーイメージ:
青もしくはグレー。
パッケージカラーに合わせて、ボトル着色可能。

上記のポイントをおさえつつ、ご応募いただけますと幸いです。
通常のパッケージデザインに加え、ボトル全体を使ったデザイン等、
自由で面白い提案も幅広く募集します!

また、ご応募の際、デザインコンセプトの説明もお願いいたします。
(一言でも構いません)

皆様のご応募心よりお待ちしております!!

※デザイン提案の注意点
ボトルデザインでは、著作権の盗用や侵害するデザイン案は一切厳禁になります。
イラスト素材テンプレの流用やアレンジも一切不可です。
記載項目
サイズ:
・大(500ml)ボトル:H177.0/W75.6
※添付ファイル「大ボトル」
・小(50ml)ボトル:H7.2/W3.1
※添付ファイル「小ボトル」

```html
<!DOCTYPE html>
<html lang="ja">
<head>
<meta charset="utf-8">
<title>ソフィネット 除菌消臭剤 パッケージ</title>
<link href="https://fonts.googleapis.com/css2?family=M+PLUS+Rounded+1c:wght@500;700;800&display=swap" rel="stylesheet">
<style>
  :root {
    --bg: #ffffff;
    --bottle-blue: #a8cdef;
    --collar-teal: #b9e3e0;
    --sprayer-clear: #eaf1f7;
    --sprayer-edge: #c8d6e3;
    --lever-blue: #7fbfe6;
    --cap-white: #f4f6f8;
    --cap-edge: #d9dfe5;
    --mascot-white: #ffffff;
    --label-text: #6ea3d6;
    --type-white: #ffffff;
  }
  html, body {
    margin: 0;
    padding: 0;
    width: 846px;
    height: 1200px;
    overflow: hidden;
    background: var(--bg);
  }
  .package-board {
    display: block;
    width: 846px;
    height: 1200px;
  }
  .product-name {
    font-family: "M PLUS Rounded 1c", sans-serif;
    font-weight: 800;
    fill: var(--type-white);
  }
  .product-kana {
    font-family: "M PLUS Rounded 1c", sans-serif;
    font-weight: 700;
    fill: var(--type-white);
  }
  .product-type {
    font-family: "M PLUS Rounded 1c", sans-serif;
    font-weight: 700;
    fill: var(--label-text);
  }
  .type-badge { fill: var(--type-white); }
  .bottle-body { fill: var(--bottle-blue); }
  .neck-collar { fill: var(--collar-teal); }
  .mascot-area { fill: var(--mascot-white); }
  .sprayer-part { fill: var(--sprayer-clear); stroke: var(--sprayer-edge); stroke-width: 2; }
  .sprayer-lever { fill: var(--lever-blue); }
  .mist-cap { fill: var(--cap-white); stroke: var(--cap-edge); stroke-width: 2; }
</style>
</head>
<body>
<svg class="package-board" viewBox="0 0 846 1200" xmlns="http://www.w3.org/2000/svg">

  <!-- Large 500ml bottle -->
  <g class="bottle bottle-large">
    <g class="trigger-sprayer" role="img" aria-label="Clear trigger sprayer with a blue lock lever">
      <path class="sprayer-part trigger" d="M436 282 Q500 300 532 378 Q556 440 566 492 Q550 498 538 468 Q508 390 452 336 Z"/>
      <path class="sprayer-part shroud" d="M282 282 H446 L424 350 H298 Z"/>
      <rect class="sprayer-part nozzle" x="190" y="244" width="90" height="40" rx="10"/>
      <rect class="sprayer-part nozzle-tip" x="178" y="250" width="18" height="28" rx="4"/>
      <rect class="sprayer-part head" x="252" y="212" width="222" height="80" rx="32"/>
      <rect class="sprayer-lever" x="414" y="318" width="34" height="24" rx="5"/>
      <rect class="sprayer-lever" x="440" y="324" width="22" height="12" rx="4"/>
    </g>
    <rect class="neck-collar" x="284" y="346" width="96" height="68" rx="10"/>
    <path class="bottle-body"
          d="M300 408 H364 Q372 408 378 418 L440 470 Q452 480 452 498 V1004 Q452 1030 426 1030 H210 Q184 1030 184 1004 V498 Q184 480 196 470 L286 418 Q292 408 300 408 Z"/>
    <rect class="mascot-area" x="220" y="522" width="197" height="141"
          role="img" aria-label="Penguin mascot head in navy and white"/>
    <text class="product-name" x="230" y="770" font-size="76">Sofi</text>
    <text class="product-name" x="230" y="846" font-size="76">net</text>
    <text class="product-kana" x="232" y="892" font-size="30">ソフィネット</text>
    <rect class="type-badge" x="231" y="908" width="178" height="45" rx="6"/>
    <text class="product-type" x="320" y="941" font-size="28" text-anchor="middle">除菌消臭剤</text>
  </g>

  <!-- Small 50ml bottle -->
  <g class="bottle bottle-small">
    <rect class="mist-cap" x="578" y="705" width="57" height="102" rx="8"
          role="img" aria-label="White mist spray cap"/>
    <path class="bottle-body"
          d="M582 804 H631 L648 822 Q654 828 654 838 V1062 Q654 1072 644 1072 H568 Q558 1072 558 1062 V838 Q558 828 564 822 Z"/>
    <rect class="mascot-area" x="568" y="846" width="76" height="70"
          role="img" aria-label="Penguin mascot head in navy and white"/>
    <text class="product-name" x="566" y="962" font-size="30">Sofi</text>
    <text class="product-name" x="566" y="996" font-size="30">net</text>
    <text class="product-kana" x="567" y="1018" font-size="12">ソフィネット</text>
    <rect class="type-badge" x="566" y="1026" width="72" height="20" rx="3"/>
    <text class="product-type" x="602" y="1041" font-size="12" text-anchor="middle">除菌消臭剤</text>
  </g>

</svg>
</body>
</html>
```